Square graphic for social media post

I want to create a 1080 x 1080px all-black image for the quote below that I can share on social media. I want the emphasis to be primarily on the quote, secondarily on the portrait, and third (smallest) on the logo. I want the background on the portrait to be edited so it's transparent and just shows the face of the person on a black background (no brick wall visible).

Graphic color: black
Text color: white
Content: "What we went through is going to make the greatest generation of hoteliers our industry has ever seen." << biggest text
Dorian Welk << smaller text
President, Marrowgate Hotels << smaller text
[image of person - use whichever version looks better to you]
[Add Lodging Ledger logo - whichever looks better to you]

This image needs to be readable when sized down much smaller (400x400?) so want the text and portrait to take up most of the space.

I'd like the output both as PNG and original file (preferably Canva). Thanks!

Target Market(s)

Hotel managers

Industry/Entity Type

Hospitality

Font styles to use
Sans Serif

Colors

Designer to choose colors to be used in the design.

Requirements
Must have
• Needs to focus on the quote and the person quoted (the portrait)

```html
<!DOCTYPE html>
<html lang="en">
<head>
<meta charset="UTF-8">
<title>Dorian Welk Quote — Lodging Ledger</title>
<link rel="stylesheet" href="https://fonts.googleapis.com/css2?family=Arvo:wght@400;700&family=Oswald:wght@400;600&display=swap">
<style>
  :root {
    --bg: #000000;
    --ink: #ffffff;
    --portrait-light: #6e6e6e;
    --portrait-mid: #333333;
    --portrait-dark: #050505;
  }
  html, body {
    margin: 0;
    padding: 0;
    background: var(--bg);
    overflow: hidden;
  }
  .post {
    position: relative;
    width: 1200px;
    height: 1200px;
    background: var(--bg);
    overflow: hidden;
    color: var(--ink);
  }
  .portrait {
    position: absolute;
    left: 0;
    top: 0;
    width: 640px;
    height: 1200px;
    background:
      radial-gradient(ellipse 300px 380px at 300px 520px, var(--portrait-light) 0%, var(--portrait-mid) 55%, transparent 100%),
      radial-gradient(ellipse 360px 420px at 290px 1120px, #4a4a4a 0%, #1a1a1a 60%, transparent 100%),
      linear-gradient(90deg, var(--portrait-dark) 0%, #111 45%, var(--bg) 100%);
  }
  .masthead {
    position: absolute;
    left: 872px;
    top: 150px;
    transform: translateX(-50%);
    display: flex;
    align-items: center;
    gap: 14px;
    white-space: nowrap;
  }
  .masthead-dot {
    width: 14px;
    height: 14px;
    border-radius: 50%;
    background: var(--ink);
  }
  .masthead-name {
    font-family: "Arvo", serif;
    font-weight: 700;
    font-size: 34px;
    letter-spacing: 4px;
    text-transform: uppercase;
    color: var(--ink);
  }
  .quote {
    position: absolute;
    left: 600px;
    width: 556px;
    top: 340px;
    margin: 0;
    font-family: "Arvo", serif;
    font-weight: 400;
    font-size: 58px;
    line-height: 69px;
    text-align: center;
    color: var(--ink);
  }
  .attribution {
    position: absolute;
    left: 669px;
    top: 1052px;
  }
  .attribution-name {
    display: inline-block;
    font-family: "Oswald", sans-serif;
    font-weight: 600;
    font-size: 46px;
    line-height: 1;
    text-transform: uppercase;
    letter-spacing: 1px;
    padding-bottom: 4px;
    border-bottom: 2px solid var(--ink);
  }
  .attribution-role {
    margin-top: 8px;
    font-family: "Oswald", sans-serif;
    font-weight: 400;
    font-size: 26px;
    line-height: 1;
    text-transform: uppercase;
  }
</style>
</head>
<body>
  <main class="post">
    <div class="portrait" role="img" aria-label="Black-and-white portrait of Dorian Welk, smiling, in an open-collar shirt and dark jacket, on a black background"></div>

    <div class="masthead">
      <span class="masthead-dot"></span>
      <span class="masthead-name">Lodging Ledger</span>
    </div>

    <blockquote class="quote">“What we went through is going to make the greatest generation of hoteliers our industry has ever seen”</blockquote>

    <div class="attribution">
      <div class="attribution-name">Dorian Welk</div>
      <div class="attribution-role">President, Marrowgate Hotels</div>
    </div>
  </main>
</body>
</html>
```